Mirabo & Orvan Automotive Repair Shop. Need a new website design.

We specialize in Mirabo & Orvan auto repair, but also work on other Asian import vehicles. We have been in business for 7 years and pride ourselves on high quality auto repair that is fixed right the first time. Would like the automotive repair website to incorporate the colors black, red and white if possible and have our logo and some Mirabo and Orvan vehicles included in the website.

Target Market(s)

Mirabo & Orvan vehicle owners

Industry/Entity Type

Automotive Repair

Coding

Coded - Design and coding required

Number of Pages Required

5+ page

Colors
EB3D1F
EC4F4E
F09395
F8D3D4
FCEDEE

Requirements
Must have
• Home, Services, Contact Us, Schedule appointment, and a gallery tab that I can add shop pictures to when completed.
Nice to have
• Would like to see example pictures of job next to each service listed.
Should not have
• Service not related to auto repair. Ex. auto detailing, towing, car wash

```html
<!DOCTYPE html>
<html lang="en">
<head>
<meta charset="utf-8">
<title>Halden Automotive Repairs</title>
<link href="https://fonts.googleapis.com/css2?family=Oswald:wght@500&family=Outfit:wght@400;500;600;700&display=swap" rel="stylesheet">
<style>
:root{--red:#EB3D1F;--red2:#EC4F4E;--rose:#F09395;--blush:#F8D3D4;--pale:#FCEDEE;--ink:#111;--dark:#161616;--white:#fff;--grey:#444}
*{box-sizing:border-box;margin:0;padding:0}
html,body{width:1200px;height:5008px;overflow:hidden}
body{font-family:'Outfit',sans-serif;color:var(--ink);background:var(--white);position:relative}
.abs{position:absolute}
.photo{position:absolute}
.brand{display:flex;align-items:center;gap:8px;font-weight:700;color:var(--white);font-size:26px;letter-spacing:1px}
.brand .dot{width:22px;height:22px;border-radius:50%;background:var(--red)}
.hero{position:absolute;left:0;top:0;width:1200px;height:615px;overflow:hidden}
.nav a{position:absolute;top:44px;font-size:13px;color:var(--white);text-decoration:none;font-weight:500}
.nav .active{color:var(--red)}
.cta-tab{position:absolute;background:var(--red);color:var(--white);font-size:12px;font-weight:600;display:flex;align-items:center;justify-content:center;clip-path:polygon(6% 0,100% 0,94% 100%,0 100%)}
.hero h1{position:absolute;left:142px;top:212px;font-family:'Oswald',sans-serif;font-weight:500;color:var(--white);font-size:41px;line-height:55px}
.eyebrow{color:var(--red);font-size:20px;font-weight:500}
.title{font-weight:700;font-size:23px;text-transform:uppercase}
.center{position:absolute;left:0;width:1200px;text-align:center}
.btn{position:absolute;background:var(--red2);color:var(--white);font-size:12px;font-weight:600;border-radius:8px;display:flex;align-items:center;justify-content:center;text-transform:uppercase;box-shadow:0 4px 10px rgba(235,61,31,.3)}
.card{position:absolute;width:293px;height:293px;border-radius:14px;overflow:hidden;color:var(--white);text-align:center}
.card .txt{position:absolute;left:0;right:0;bottom:34px}
.card h3{font-size:14px;font-weight:600;text-transform:uppercase;margin-bottom:6px}
.card p{font-size:10.5px;line-height:19px;padding:0 24px}
.card .more{display:block;margin-top:6px;color:var(--red);font-size:11px;font-weight:700;text-decoration:underline}
.card.featured{outline:4px solid var(--red);outline-offset:-4px}
.gimg{position:absolute;border:3px solid var(--white);border-radius:12px}
.field{position:absolute;height:36px;border:1px solid #ddd;border-radius:6px;background:var(--white);font-size:11px;color:#555;padding:11px 16px}
.field.on{border-color:var(--red2)}
.field svg{position:absolute;right:12px;top:10px}
.icon-circle{position:absolute;width:34px;height:34px;border-radius:50%;background:var(--red2);display:flex;align-items:center;justify-content:center}
</style>
</head>
<body>

<header class="hero">
  <div class="photo" role="img" aria-label="Mechanic checking an engine under a raised car hood in a workshop" style="inset:0;background:linear-gradient(90deg,#050505 0%,#141414 35%,#3d4550 65%,#7c8590 85%,#a6acb3 100%)"></div>
  <div class="brand abs" style="left:142px;top:48px">HALDEN<span class="dot"></span></div>
  <nav class="nav">
    <a class="active" style="left:465px">HOME</a>
    <a style="left:553px">SERVICES</a>
    <a style="left:667px">ABOUT US</a>
    <a style="left:783px">DIRECTIONS</a>
  </nav>
  <div class="cta-tab" style="left:918px;top:34px;width:138px;height:34px">CONTACT US »</div>
  <h1>Authorized Installer For<br>Duravex Oil, Keystone Battery</h1>
  <div class="abs" aria-label="Local award badge" style="left:142px;top:345px;width:98px;height:88px;border-radius:50%;background:#1a6fa8"></div>
  <div class="abs" aria-label="Certification badge" style="left:265px;top:343px;width:86px;height:86px;border-radius:50%;background:#2577c4"></div>
  <div class="cta-tab" style="left:143px;top:455px;width:240px;height:34px">SCHEDULE AN APPOINTMENT »</div>
</header>

<section class="about">
  <div class="photo" role="img" aria-label="Smiling mechanic in blue overalls holding a wrench" style="left:287px;top:703px;width:328px;height:497px;background:linear-gradient(160deg,#c9ccd0,#3a4a78 60%,#243a8a)"></div>
  <div class="photo" role="img" aria-label="Close-up of a car engine bay with red parts" style="left:140px;top:985px;width:310px;height:292px;background:linear-gradient(140deg,#222,#5b1d14 70%,#b52a1a)"></div>
  <div class="abs" style="left:142px;top:820px;width:202px;height:115px;background:var(--white);box-shadow:0 8px 24px rgba(0,0,0,.15);padding:22px 28px">
    <div style="color:var(--red);font-size:40px;font-weight:600;line-height:1">7+</div>
    <div style="font-size:19px;line-height:28px;margin-top:6px">Years of<br>Experience</div>
    <div class="abs" style="right:26px;top:24px;width:34px;height:34px;border-radius:50%;background:var(--red)"></div>
  </div>
  <div class="abs" style="left:672px;top:808px;width:390px">
    <div class="eyebrow">About Us</div>
    <div class="title" style="margin-top:20px">Halden Automotive Repairs</div>
    <p style="font-size:12px;line-height:21.5px;margin-top:16px">Here at Halden Automotive, we believe in professional service and high quality auto repairs. With 7 years in business and deep Mirabo, Orvan, &amp; Sella expertise, we have all the tools, equipment, and knowledge to keep your Mirabo, Orvan, &amp; Sella vehicle running strong. Although we specialize in these makes, we also repair &amp; service other import makes like Kaito, Arden, Nisora, Inveris, Kivo, Hyoran, Mitsura, etc. At Halden Automotive, we are dedicated to providing an atmosphere where people feel comfortable knowing that their vehicle will be repaired correctly and only repairs that are needed are recommended. Free Shuttle Rides are available</p>
  </div>
  <div class="btn" style="left:672px;top:1132px;width:121px;height:38px">Contact</div>
</section>

<section class="services abs" style="left:0;top:1365px;width:1200px;height:945px;background:var(--pale)">
  <div class="center eyebrow" style="top:65px">Services</div>
  <div class="center title" style="top:104px">Halden Automotive Repairs</div>
  <div class="card" style="left:140px;top:181px"><div class="photo" role="img" aria-label="Oil being poured into an engine" style="inset:0;background:linear-gradient(180deg,#2c4a6b,#111)"></div><div class="txt"><h3>Oil Changes</h3><p>Lorem ipsum dolor sit amet, consectetur adipiscing elit, sed do eiusmod tempor incididunt</p><span class="more">READ MORE</span></div></div>
  <div class="card" style="left:453px;top:181px"><div class="photo" role="img" aria-label="Technician running computer diagnostics on a car" style="inset:0;background:linear-gradient(180deg,#4a5560,#111)"></div><div class="txt"><h3>Computer Diagnostics</h3><p>Lorem ipsum dolor sit amet, consectetur adipiscing elit, sed do eiusmod tempor incididunt</p><span class="more">READ MORE</span></div></div>
  <div class="card" style="left:766px;top:181px"><div class="photo" role="img" aria-label="Car wheel and tire close-up" style="inset:0;background:linear-gradient(180deg,#5a4a40,#111)"></div><div class="txt"><h3>Tire Balance &amp; Rotations</h3><p>Lorem ipsum dolor sit amet, consectetur adipiscing elit, sed do eiusmod tempor incididunt</p><span class="more">READ MORE</span></div></div>
  <div class="card" style="left:140px;top:495px"><div class="photo" role="img" aria-label="Mechanics working on an engine" style="inset:0;background:linear-gradient(180deg,#555,#111)"></div><div class="txt"><h3>Engine Repair</h3><p>Lorem ipsum dolor sit amet, consectetur adipiscing elit, sed do eiusmod tempor incididunt</p><span class="more">READ MORE</span></div></div>
  <div class="card" style="left:453px;top:495px"><div class="photo" role="img" aria-label="Brake work on a raised car" style="inset:0;background:linear-gradient(180deg,#3c4a58,#111)"></div><div class="txt"><h3>Brake Service &amp; Repair</h3><p>Lorem ipsum dolor sit amet, consectetur adipiscing elit, sed do eiusmod tempor incididunt</p><span class="more">READ MORE</span></div></div>
  <div class="card featured" style="left:766px;top:495px"><div class="photo" role="img" aria-label="Technician servicing a transmission under a dark car" style="inset:0;background:linear-gradient(180deg,#5c5c5c,#111)"></div><div class="txt"><h3>Transmission Service</h3><p>Lorem ipsum dolor sit amet, consectetur adipiscing elit, sed do eiusmod tempor incididunt</p><span class="more">READ MORE</span></div></div>
  <div class="btn" style="left:512px;top:835px;width:176px;height:38px;border-radius:10px">View All Services</div>
</section>

<section class="testimonials">
  <div class="center title" style="top:2393px">Client Testimonials</div>
  <div class="abs" style="left:582px;top:2447px;width:36px;height:36px;border-radius:50%;background:var(--red2)">
    <svg width="36" height="36" viewBox="0 0 36 36"><path d="M11 22c0-5 2-8 5-9v3c-1.5.7-2 2-2 3h2v5h-5zM19 22c0-5 2-8 5-9v3c-1.5.7-2 2-2 3h2v5h-5z" fill="#fff"/></svg>
  </div>
  <p class="center" style="top:2500px;left:210px;width:780px;font-size:13px;line-height:21px;color:var(--grey)">Lorem ipsum dolor sit amet, consectetur adipiscing elit, sed do eiusmod tempor incididunt ut labore et dolore magna aliqua. Ut enim ad minim veniam, quis nostrud exercitation ullamco laboris nisi ut aliquip ex ea commodo consequat. Duis aute irure dolor in reprehenderit in voluptate velit esse cillum dolore eu fugiat nulla pariatur. Excepteur sint occaecat cupidatat non proident, sunt in culpa qui officia deserunt mollit anim id est laborum.</p>
  <svg class="abs" style="left:98px;top:2520px" width="44" height="44" viewBox="0 0 44 44"><circle cx="22" cy="22" r="21" fill="#fff" stroke="#EC4F4E" stroke-width="1.5"/><path d="M29 22H15m5-5-5 5 5 5" stroke="#EC4F4E" stroke-width="2" fill="none"/></svg>
  <svg class="abs" style="left:1057px;top:2520px" width="44" height="44" viewBox="0 0 44 44"><circle cx="22" cy="22" r="22" fill="#EC4F4E"/><path d="M15 22h14m-5-5 5 5-5 5" stroke="#fff" stroke-width="2" fill="none"/></svg>
  <div class="photo" role="img" aria-label="Client portrait" style="left:564px;top:2600px;width:70px;height:70px;border-radius:50%;background:linear-gradient(180deg,#cfd3d8,#7a8a9a)"></div>
  <div class="center" style="top:2684px;font-size:15px;font-weight:600">Sam Porter</div>
</section>

<section class="gallery abs" style="left:0;top:2770px;width:1200px;height:725px">
  <div class="photo" role="img" aria-label="Dark workshop backdrop" style="inset:0;background:linear-gradient(180deg,#1a1a1a,#0c0c0c)"></div>
  <div class="center eyebrow" style="top:64px">Gallery</div>
  <div class="center title" style="top:106px;color:var(--white)">Halden Automotive Repairs</div>
  <div class="gimg photo" role="img" aria-label="Mechanic holding a tire in a garage" style="left:-10px;top:310px;width:195px;height:182px;background:linear-gradient(160deg,#e3e3e3,#777)"></div>
  <div class="gimg photo" role="img" aria-label="Mechanic beside a red tool chest" style="left:213px;top:206px;width:238px;height:181px;background:linear-gradient(160deg,#8a929c,#3a1414)"></div>
  <div class="gimg photo" role="img" aria-label="Mechanic working under an open hood" style="left:213px;top:413px;width:238px;height:182px;background:linear-gradient(160deg,#4c7ab0,#222)"></div>
  <div class="gimg photo" role="img" aria-label="Mechanic leaning over the engine of a dark car" style="left:481px;top:183px;width:238px;height:437px;background:linear-gradient(180deg,#b8bec4,#2a3550 70%,#1a2240)"></div>
  <div class="gimg photo" role="img" aria-label="Two mechanics inspecting a silver car" style="left:750px;top:206px;width:238px;height:181px;background:linear-gradient(160deg,#d0d4d8,#4a5058)"></div>
  <div class="gimg photo" role="img" aria-label="Mechanic checking an engine in a bright workshop" style="left:750px;top:413px;width:238px;height:182px;background:linear-gradient(160deg,#e4e6e8,#3d4a5c)"></div>
  <div class="gimg photo" role="img" aria-label="Car on a lift in a service bay" style="left:1015px;top:310px;width:195px;height:182px;background:linear-gradient(160deg,#b06a3a,#2a2420)"></div>
</section>

<section class="contact">
  <div class="center eyebrow" style="top:3582px">Contact Us</div>
  <div class="center title" style="top:3622px">Halden Automotive Repairs</div>
  <div class="abs" style="left:140px;top:3683px;width:920px;height:432px;background:var(--pale)"></div>
  <div class="photo" role="img" aria-label="Technician working on an engine" style="left:140px;top:3683px;width:335px;height:432px;background:linear-gradient(160deg,#7a6a60,#2a2626 55%,#121212)"></div>
  <div class="icon-circle" style="left:187px;top:3951px"><svg width="16" height="16" viewBox="0 0 24 24"><path d="M6 2l4 4-2 3a12 12 0 0 0 7 7l3-2 4 4-3 4C10 22 2 14 2 5z" fill="none" stroke="#fff" stroke-width="2"/></svg></div>
  <div class="abs" style="left:233px;top:3950px;color:var(--white)"><div style="font-size:10px;font-weight:700">CALL US TODAY:</div><div style="font-size:13px;margin-top:4px">555-201-7493</div></div>
  <div class="icon-circle" style="left:187px;top:4020px"><svg width="16" height="16" viewBox="0 0 24 24"><rect x="3" y="5" width="18" height="14" rx="2" fill="none" stroke="#fff" stroke-width="2"/><path d="M3 7l9 6 9-6" fill="none" stroke="#fff" stroke-width="2"/></svg></div>
  <div class="abs" style="left:233px;top:4020px;color:var(--white)"><div style="font-size:10px;font-weight:700">EMAIL ADDRESS:</div><div style="font-size:13px;margin-top:4px">haldenautollc@mail.example</div></div>
  <div class="field on" style="left:515px;top:3770px;width:245px">First Name<svg width="14" height="14" viewBox="0 0 24 24"><circle cx="12" cy="8" r="4" fill="none" stroke="#999" stroke-width="2"/><path d="M4 21c1-5 15-5 16 0" fill="none" stroke="#999" stroke-width="2"/></svg></div>
  <div class="field" style="left:773px;top:3770px;width:247px">Last Name<svg width="14" height="14" viewBox="0 0 24 24"><circle cx="12" cy="8" r="4" fill="none" stroke="#999" stroke-width="2"/><path d="M4 21c1-5 15-5 16 0" fill="none" stroke="#999" stroke-width="2"/></svg></div>
  <div class="field" style="left:515px;top:3818px;width:245px">Email Address<svg width="16" height="14" viewBox="0 0 24 20"><rect x="2" y="2" width="20" height="16" rx="2" fill="none" stroke="#999" stroke-width="2"/><path d="M2 4l10 7 10-7" fill="none" stroke="#999" stroke-width="2"/></svg></div>
  <div class="field" style="left:773px;top:3818px;width:247px">Phone<svg width="14" height="14" viewBox="0 0 24 24"><path d="M6 2l4 4-2 3a12 12 0 0 0 7 7l3-2 4 4-3 4C10 22 2 14 2 5z" fill="none" stroke="#999" stroke-width="2"/></svg></div>
  <div class="field" style="left:515px;top:3868px;width:505px;height:137px">Message<svg width="16" height="16" viewBox="0 0 24 24"><circle cx="12" cy="12" r="9" fill="none" stroke="#999" stroke-width="2"/></svg></div>
  <div class="btn" style="left:515px;top:4048px;width:122px;height:38px">Submit</div>
</section>

<section class="schedule abs" style="left:0;top:4205px;width:1200px;height:345px">
  <div class="photo" role="img" aria-label="Dark garage backdrop" style="inset:0;background:linear-gradient(180deg,#141414,#202020)"></div>
  <div class="center" style="top:72px;color:var(--red);font-size:29px;font-weight:600">Schedule an Appointment Today!</div>
  <p class="center" style="top:132px;left:150px;width:900px;color:var(--white);font-size:11.5px;line-height:21px">Receive top notch, honest, reliable service from our team with 7 years in business and a focus on Mirabo &amp; Orvan repair. Owner is an NTA Certified Master Technician who has experience managing an entire team of technicians in big name dealerships, assisting them in their diagnosis &amp; repair work. What does this mean for you, our loyal customer? It means you are entrusting your vehicle to highly trained specialists.</p>
  <div class="btn" style="left:492px;top:227px;width:216px;height:38px">Request Appointment</div>
</section>

<footer class="abs" style="left:0;top:4550px;width:1200px;height:458px;background:var(--pale)">
  <div class="photo" role="img" aria-label="Dark grey pickup truck" style="left:22px;top:-130px;width:370px;height:220px;border-radius:40px 60px 30px 30px;background:linear-gradient(180deg,#555,#1c1c1c)"></div>
  <div class="brand abs" style="left:0;width:1200px;justify-content:center;top:125px;color:var(--ink);font-size:34px">HALDEN<span class="dot"></span></div>
  <div class="center" style="top:266px;font-size:12px">Home &nbsp;|&nbsp; About Us &nbsp;|&nbsp; Service &nbsp;|&nbsp; Gallery &nbsp;|&nbsp; Contact</div>
  <div class="icon-circle" style="left:220px;top:333px"><svg width="16" height="16" viewBox="0 0 24 24"><path d="M6 2l4 4-2 3a12 12 0 0 0 7 7l3-2 4 4-3 4C10 22 2 14 2 5z" fill="#fff"/></svg></div>
  <div class="abs" style="left:266px;top:342px;font-size:12px">555-201-7493</div>
  <div class="icon-circle" style="left:400px;top:333px"><svg width="16" height="16" viewBox="0 0 24 24"><rect x="3" y="5" width="18" height="14" rx="2" fill="#fff"/><path d="M3 7l9 6 9-6" fill="none" stroke="#EC4F4E" stroke-width="2"/></svg></div>
  <div class="abs" style="left:446px;top:342px;font-size:12px">haldenautollc@mail.example</div>
  <div class="icon-circle" style="left:678px;top:333px"><svg width="16" height="16" viewBox="0 0 24 24"><path d="M12 2a7 7 0 0 0-7 7c0 5 7 13 7 13s7-8 7-13a7 7 0 0 0-7-7z" fill="#fff"/><circle cx="12" cy="9" r="2.5" fill="#EC4F4E"/></svg></div>
  <div class="abs" style="left:724px;top:342px;font-size:12px">412 Harbor Point Way #5 Brookdale, TX 75000</div>
  <div class="abs" style="left:0;top:418px;width:1200px;height:40px;background:var(--red2)">
    <div class="abs" style="left:142px;top:13px;color:var(--white);font-size:11px">© 2024 Halden Automotive LLC</div>
    <svg class="abs" style="left:910px;top:7px" width="150" height="28" viewBox="0 0 150 28"><circle cx="14" cy="14" r="12.5" fill="none" stroke="#fff" stroke-width="1.5"/><circle cx="54" cy="14" r="12.5" fill="none" stroke="#fff" stroke-width="1.5"/><circle cx="94" cy="14" r="12.5" fill="none" stroke="#fff" stroke-width="1.5"/><circle cx="134" cy="14" r="12.5" fill="none" stroke="#fff" stroke-width="1.5"/></svg>
  </div>
</footer>

</body>
</html>
```